Business Card for premium dental clinic

We are a premium dental clinic based in Brasov, Romania with more than 15 year on the market, providing quality dental treatment made by a team of more specialized dentists, working with modern equipment as a solution to beautiful and healthy teeth.

Our current logo for the clinic use 2 square with colors black and gold - dr Merinca - studio, using family fonts Bodoni, Myriad Pro and Segoe Print.
Depending on the printing we used some gold CMYK background or gold foil picture background or a gold gradient.
We want a business card:
- eye catching business card
- distinguished business card
- premium design
- to keep the color scheme of black and gold
- to attract the customers to spent time reading the information
- modern concept

```html
<!DOCTYPE html>
<html lang="en">
<head>
<meta charset="utf-8">
<title>Merinca – Business Card</title>
<link rel="stylesheet" href="https://fonts.googleapis.com/css2?family=Arimo:wght@700&family=Lato:wght@400;700&display=swap">
<style>
  :root {
    --backdrop: #e9e6e2;
    --card-light: #f7f6f5;
    --card-dark: #1d1c21;
    --gold: #c0912d;
    --text-grey: #c9c9c9;
    --address-grey: #a9a9a9;
  }
  * { margin: 0; padding: 0; box-sizing: border-box; }
  html, body {
    width: 1200px;
    height: 900px;
    overflow: hidden;
    background: var(--backdrop);
  }
  .card {
    position: absolute;
    left: 150px;
    top: 172px;
    width: 900px;
    height: 556px;
    background: var(--card-light);
    box-shadow: 0 10px 30px rgba(0,0,0,0.18);
    overflow: hidden;
  }
  .card-top {
    position: absolute;
    left: 0; top: 0;
    width: 100%;
    height: 303px;
    display: flex;
    align-items: center;
    justify-content: center;
  }
  .brand-name {
    font-family: "Lato", sans-serif;
    font-weight: 400;
    font-size: 52px;
    color: var(--card-dark);
    letter-spacing: 6px;
  }
  .gold-rule {
    position: absolute;
    left: 0; top: 303px;
    width: 100%;
    height: 10px;
    background: var(--gold);
  }
  .card-bottom {
    position: absolute;
    left: 0; top: 313px;
    width: 100%;
    height: 243px;
    background: var(--card-dark);
  }
  .person {
    position: absolute;
    right: 480px;
    top: 64px;
    text-align: right;
  }
  .person-name {
    font-family: "Arimo", sans-serif;
    font-weight: 700;
    font-size: 30px;
    color: var(--gold);
    letter-spacing: 0.5px;
    line-height: 1.1;
  }
  .person-role {
    font-family: "Lato", sans-serif;
    font-size: 24px;
    color: var(--text-grey);
    margin-top: 2px;
  }
  .contacts {
    position: absolute;
    left: 478px;
    top: 46px;
    list-style: none;
  }
  .contact-item {
    display: flex;
    align-items: center;
    gap: 10px;
    height: 33px;
    font-family: "Lato", sans-serif;
    font-size: 24px;
    color: var(--text-grey);
  }
  .contact-icon { width: 20px; height: 20px; flex: none; }
  .address {
    position: absolute;
    left: 0; width: 100%;
    top: 164px;
    text-align: center;
    font-family: "Lato", sans-serif;
    font-size: 24px;
    color: var(--address-grey);
  }
</style>
</head>
<body>
  <div class="card">
    <div class="card-top">
      <span class="brand-name">MERINCA</span>
    </div>
    <div class="gold-rule"></div>
    <div class="card-bottom">
      <div class="person">
        <div class="person-name">ANDREI COSTEA</div>
        <div class="person-role">Managing Director</div>
      </div>
      <ul class="contacts">
        <li class="contact-item">
          <svg class="contact-icon" viewBox="0 0 20 20" aria-hidden="true">
            <path fill="#c0912d" d="M2 7c0-3 4-4 8-4s8 1 8 4v1h-4V6H6v2H2z"/>
            <path fill="#c0912d" d="M5 9h10l2 8H3z"/>
            <circle cx="10" cy="13" r="2" fill="#1d1c21"/>
          </svg>
          <span>0268-410 275 936</span>
        </li>
        <li class="contact-item">
          <svg class="contact-icon" viewBox="0 0 20 20" aria-hidden="true">
            <rect x="2" y="5" width="16" height="11" fill="#c0912d"/>
            <path d="M2 5l8 6 8-6" fill="none" stroke="#1d1c21" stroke-width="1.5"/>
          </svg>
          <span>hello@merincaclinic.ro</span>
        </li>
        <li class="contact-item">
          <svg class="contact-icon" viewBox="0 0 20 20" aria-hidden="true">
            <circle cx="10" cy="10" r="8" fill="#c0912d"/>
            <path d="M4 8c2 0 3 1 3 3s2 2 2 4M12 3c0 2 2 3 4 3" fill="none" stroke="#1d1c21" stroke-width="1.5"/>
          </svg>
          <span>www.merincaclinic.ro</span>
        </li>
      </ul>
      <div class="address">421, Address line goes here, 45452,Country Name</div>
    </div>
  </div>
</body>
</html>
```